Letterhead, envelope & business card design

We would like to refresh the look and feel of our business cards & letterheads.

Our company specialises in premium property.

We are looking for a unique minimalist design for our letterhead & business cards that project this.

I can send over examples of our current design to draw from, although Im looking for some one with creativity, yet focussed on a clean modern, minimalist design.
Updates

I have just uploaded our current letterhead.

We have just removed the 'swoosh' grey symbol, but would still like to keep some part of grey in the design if possible.

thanks in advance.

Just uploaded my details for business card.

Can we see examples with the light grey used as the secondary color?

thanks in advance.

Target Market(s)

We are a premium real estate agency & we want that message to be carried through our business cards & stationery.

Industry/Entity Type

Business

```html
<!DOCTYPE html>
<html lang="en">
<head>
<meta charset="utf-8">
<title>Hartwell Estate Agents – Stationery</title>
<link href="https://fonts.googleapis.com/css2?family=Cinzel:wght@500&family=Arimo:wght@400&display=swap" rel="stylesheet">
<style>
  :root {
    --page: #ffffff;
    --stage: #eceef0;
    --band-light: #2389ad;
    --band-mid: #1a7396;
    --band-dark: #14465e;
    --navy: #1b4459;
    --ink-grey: #8b8d90;
    --rule-grey: #9aa0a8;
    --faint-grey: #d7dae0;
    --shadow: 0 3px 10px rgba(0,0,0,.22);
  }
  * { box-sizing: border-box; margin: 0; padding: 0; }
  html, body { width: 1197px; height: 1200px; overflow: hidden; background: var(--page); }
  body { position: relative; font-family: "Arimo", Arial, sans-serif; }

  .sheet { position: absolute; background: var(--page); box-shadow: var(--shadow); overflow: hidden; }
  .band { position: absolute; background: linear-gradient(90deg, var(--band-mid) 0%, var(--band-light) 45%, var(--band-dark) 100%); }
  .wordmark { font-family: "Cinzel", "Times New Roman", serif; font-weight: 500; letter-spacing: .02em; line-height: 1; white-space: nowrap; }

  /* Business card – back */
  .card-back { left: 43px; top: 63px; width: 487px; height: 284px; }
  .card-back .band { left: 0; top: 112px; width: 100%; height: 58px; }
  .card-back .wordmark { position: absolute; right: 42px; top: 125px; font-size: 34px; color: #fff; }
  .contact { position: absolute; left: 24px; padding-left: 12px; border-left: 1.5px solid var(--rule-grey); color: var(--ink-grey); font-size: 13px; line-height: 16.5px; }
  .contact .email { font-size: 9px; line-height: 13px; }
  .contact.sales { top: 12px; }
  .contact.leasing { top: 186px; }

  /* Business card – front */
  .card-front { left: 43px; top: 386px; width: 487px; height: 284px; }
  .card-front .band { left: 0; top: 113px; width: 227px; height: 57px; }
  .card-front .wordmark { position: absolute; left: 254px; top: 120px; font-size: 35px; color: var(--navy); }
  .card-front .web { position: absolute; left: 270px; top: 156px; font-size: 12.5px; color: var(--ink-grey); }

  /* Letterhead */
  .letterhead { left: 600px; top: 30px; width: 557px; height: 797px; }
  .letterhead .band { left: 0; top: 49px; width: 461px; height: 53px; }
  .letterhead .wordmark.head { position: absolute; left: 8px; top: 64px; font-size: 24px; color: #fff; }
  .letterhead .wordmark.footer { position: absolute; left: 110px; top: 700px; font-size: 60px; color: var(--faint-grey); }
  .letterhead .footer-rule { position: absolute; left: 0; right: 0; top: 763px; height: 1px; background: var(--faint-grey); }

  /* Presentation stages (flat) */
  .stage { position: absolute; background: var(--stage); }
  .stage-cards { left: 43px; top: 720px; width: 509px; height: 466px; }
  .stage-letter { left: 664px; top: 860px; width: 420px; height: 316px; }
  .mini { transform-origin: 0 0; }
  .stage-cards .card-front { left: 35px; top: 30px; transform: scale(.56); }
  .stage-cards .card-back { left: 35px; top: 220px; transform: scale(.56); }
  .stage-cards .card-front, .stage-cards .card-back { position: absolute; }
  .stage-letter .letterhead { left: 150px; top: 20px; transform: scale(.345); }
</style>
</head>
<body>

  <section class="sheet card-back" aria-label="Business card, contact side">
    <div class="contact sales">
      <p>SALES</p>
      <p>58 Harbour St</p>
      <p>Lakeview NSW 2290</p>
      <p>T. 02 5550 1888</p>
      <p>F. 02 5550 1887</p>
      <p class="email">office@hartwellestates.com.au</p>
    </div>
    <div class="band"></div>
    <p class="wordmark">HARTWELL</p>
    <div class="contact leasing">
      <p>PROPERTY MANAGEMENT</p>
      <p>58 Harbour St</p>
      <p>Lakeview NSW 2290</p>
      <p>T. 02 5550 1802</p>
      <p>F. 02 5550 1887</p>
      <p class="email">leasing@hartwellestates.com.au</p>
    </div>
  </section>

  <section class="sheet card-front" aria-label="Business card, brand side">
    <div class="band"></div>
    <p class="wordmark">HARTWELL</p>
    <p class="web">www.hartwellestates.com.au</p>
  </section>

  <section class="sheet letterhead" aria-label="Letterhead">
    <div class="band"></div>
    <p class="wordmark head">HARTWELL</p>
    <p class="wordmark footer">HARTWELL</p>
    <div class="footer-rule"></div>
  </section>

  <section class="stage stage-cards" aria-label="Business cards presentation">
    <div class="sheet card-front mini">
      <div class="band"></div>
      <p class="wordmark">HARTWELL</p>
      <p class="web">www.hartwellestates.com.au</p>
    </div>
    <div class="sheet card-back mini">
      <div class="contact sales">
        <p>SALES</p><p>58 Harbour St</p><p>Lakeview NSW 2290</p><p>T. 02 5550 1888</p><p>F. 02 5550 1887</p><p class="email">office@hartwellestates.com.au</p>
      </div>
      <div class="band"></div>
      <p class="wordmark">HARTWELL</p>
      <div class="contact leasing">
        <p>PROPERTY MANAGEMENT</p><p>58 Harbour St</p><p>Lakeview NSW 2290</p><p>T. 02 5550 1802</p><p>F. 02 5550 1887</p><p class="email">leasing@hartwellestates.com.au</p>
      </div>
    </div>
  </section>

  <section class="stage stage-letter" aria-label="Letterhead presentation">
    <div class="sheet letterhead mini">
      <div class="band"></div>
      <p class="wordmark head">HARTWELL</p>
      <p class="wordmark footer">HARTWELL</p>
      <div class="footer-rule"></div>
    </div>
  </section>

</body>
</html>
```